Love-Drama Movie Flyer for World Sales Pitch

Dear Designers

We need for a world sales pitch a flyer for our new movie MARBLEFIN. We need a front and a back page A4.
Front: One picture we deliver for then whole page, title, some "pitch" sentences
Picture Front: https://www.fileharbor-example.net/s/qk83tnb2px71vd9/Front_Picture.jpg?dl=0
Back: Arrangement of title, 5 pictures and text we deliver (attached)

Please find in the attached examples a rough idea what we’re looking for. Should not be exactly the same.

To get an Impression of the content and style of the film, please watch the 3min teaser. This will be very important for the style of the flyer:
https://clipvault-example.net/487316920
pw: tutumarblefin

In the end we prefer a data package with the flyer made in a adobe design application for high quality print.

Thanks
Tomas Vrelnik
Producer

Target Market(s)

High profile film sales professionals

Industry/Entity Type

Film Production

Requirements
Must have
• see description
Should not have
• not too generic,
• there is the color red on the actors pullover but red is not really a color in the film. So please don't use much red
• Awards of the actor/actress are not for this movie, it's from other movies

```html
<!DOCTYPE html>
<html lang="en">
<head>
<meta charset="utf-8">
<title>MARBLEFIN – Flyer Front</title>
<link rel="stylesheet" href="https://fonts.googleapis.com/css2?family=Arimo:ital,wght@0,400;0,700;1,400;1,700&display=swap">
<style>
  :root {
    --frame: #86b1b6;
    --panel-top: #8fb6ba;
    --panel-mid: #bfd9da;
    --panel-bottom: #ffffff;
    --title: #86b1b6;
    --credit: #ffffff;
    --photo-top: #3f4f53;
    --photo-bottom: #8db3b6;
  }
  * { margin: 0; padding: 0; box-sizing: border-box; }
  html, body { width: 848px; height: 1200px; overflow: hidden; background: var(--frame); }
  .flyer {
    position: relative; width: 848px; height: 1200px;
    background: var(--frame);
    font-family: "Arimo", Arial, sans-serif;
  }
  .panel {
    position: absolute; left: 22px; top: 22px; width: 804px; height: 1154px;
    background: linear-gradient(to bottom, var(--panel-top) 0%, var(--panel-mid) 50%, #e6f1f1 72%, var(--panel-bottom) 100%);
  }
  .tagline {
    position: absolute; left: 0; width: 848px; top: 40px; text-align: center;
    color: var(--credit); font-weight: 700; font-style: italic;
    font-size: 30px; letter-spacing: 3px; transform: rotate(-3deg);
  }
  .lead-photo {
    position: absolute; left: 306px; top: 104px; width: 244px; height: 768px;
    border-radius: 90px 90px 20px 20px;
    background: linear-gradient(to bottom, var(--photo-top) 0%, #55686c 45%, var(--photo-bottom) 100%);
    opacity: .9;
  }
  .credit-line {
    position: absolute; white-space: nowrap; color: var(--credit);
    font-size: 13.5px; letter-spacing: 3px; line-height: 1;
  }
  .credit-line.strong { font-weight: 700; }
  .credit-line.italic { font-style: italic; }
  .right { text-align: right; transform: translateX(-100%); }
  .actor-first { position: absolute; color: var(--credit); font-style: italic; font-size: 21px; letter-spacing: 4px; white-space: nowrap; }
  .actor-last { position: absolute; color: var(--credit); font-style: italic; font-weight: 700; font-size: 22px; letter-spacing: 3px; white-space: nowrap; }
  .title-rule { position: absolute; left: 52px; width: 744px; height: 1.5px; background: var(--title); }
  .title { position: absolute; left: 0; top: 890px; }
  .director {
    position: absolute; left: 176px; top: 1092px; color: var(--title);
    font-size: 22px; letter-spacing: 9px; white-space: nowrap;
    transform: rotate(2.2deg); transform-origin: left center;
  }
  .director b { font-weight: 700; letter-spacing: 8px; }
  .web {
    position: absolute; left: 0; width: 848px; top: 1179px; text-align: center;
    color: var(--credit); font-weight: 700; font-style: italic; font-size: 13px;
  }
</style>
</head>
<body>
<div class="flyer">
  <div class="panel"></div>
  <p class="tagline">“This is David.”</p>
  <div class="lead-photo" role="img" aria-label="Full-length photo of the lead actor standing in a dark hooded sweatshirt, hands in pockets, fading into pale teal"></div>

  <!-- left cast credits -->
  <p class="actor-first" style="left:62px;top:250px">MATTEO</p>
  <p class="actor-last" style="left:52px;top:270px">KELLNER</p>
  <p class="credit-line" style="left:52px;top:306px">Alpine</p>
  <p class="credit-line" style="left:54px;top:323px">Film</p>
  <p class="credit-line" style="left:59px;top:340px">Award</p>
  <p class="credit-line" style="left:62px;top:357px">2015</p>
  <p class="credit-line strong" style="left:66px;top:374px">BEST ACTOR</p>
  <p class="credit-line" style="left:72px;top:409px">EUROPEAN</p>
  <p class="credit-line" style="left:75px;top:426px">RISING</p>
  <p class="credit-line" style="left:78px;top:443px">STAR</p>
  <p class="credit-line strong" style="left:82px;top:460px">2015</p>
  <p class="credit-line" style="left:88px;top:494px">RECURRING</p>
  <p class="credit-line" style="left:92px;top:511px">APPEARANCE</p>
  <p class="credit-line" style="left:95px;top:528px">IN AWARD</p>
  <p class="credit-line" style="left:98px;top:545px">WINNING US</p>
  <p class="credit-line" style="left:102px;top:562px">SERIES</p>
  <p class="credit-line strong" style="left:105px;top:580px">NORTHWATCH</p>

  <!-- right cast credits -->
  <p class="actor-first right" style="left:776px;top:250px">LIORA</p>
  <p class="actor-last right" style="left:796px;top:270px;font-style:normal">FENNA BRANDT</p>
  <p class="credit-line italic right" style="left:792px;top:306px">Orion</p>
  <p class="credit-line italic right" style="left:788px;top:323px">Award</p>
  <p class="credit-line italic right" style="left:786px;top:340px">Nominee</p>
  <p class="credit-line italic right" style="left:782px;top:357px">2016</p>
  <p class="credit-line italic strong right" style="left:778px;top:374px">BEST ACTRESS</p>
  <p class="credit-line italic right" style="left:772px;top:409px">Lakeland</p>
  <p class="credit-line italic right" style="left:768px;top:426px">Film</p>
  <p class="credit-line italic right" style="left:766px;top:443px">Award</p>
  <p class="credit-line italic right" style="left:762px;top:460px">2015</p>
  <p class="credit-line italic strong right" style="left:760px;top:477px">BEST</p>
  <p class="credit-line italic strong right" style="left:756px;top:494px">YOUNG</p>
  <p class="credit-line italic strong right" style="left:753px;top:511px">ACTRESS</p>
  <p class="credit-line italic right" style="left:748px;top:546px">Fresh</p>
  <p class="credit-line italic right" style="left:744px;top:563px">Faces</p>
  <p class="credit-line italic right" style="left:741px;top:580px">Award</p>
  <p class="credit-line italic right" style="left:738px;top:597px">2012</p>
  <p class="credit-line italic strong right" style="left:734px;top:614px">BEST ACTRESS</p>

  <!-- title -->
  <div class="title-rule" style="top:872px"></div>
  <svg class="title" width="848" height="160" viewBox="0 0 848 160">
    <text x="52" y="146" textLength="744" lengthAdjust="spacingAndGlyphs"
          font-family="Arimo, Arial, sans-serif" font-weight="700" font-size="186"
          fill="var(--title)">MARBLEFIN</text>
  </svg>
  <div class="title-rule" style="top:1061px"></div>

  <p class="director">a film by <b>Adrian Solberg</b></p>
  <p class="web">www.cinderleaf-films.example</p>
</div>
</body>
</html>
```